Business Cards - Brightwell Harbor

need to design unique business card for my mortgage business. I need to design credit card style business card for my business or any unique idea that you might have

Target Market(s)

Home Loan customers

Industry/Entity Type

Mortgage Brokerage

Contact Information for Business Card

please design credit card style or very unique style business card

Colors

Designer to choose colors to be used in the design.

Requirements
Must have
• Name
• position
• Phone number
• fax number
• email address
• website address
• social media address
• All above fields will be provided once design in finalised

```html
<!DOCTYPE html>
<html lang="en">
<head>
<meta charset="utf-8">
<title>Brightwell Harbor – Business Card</title>
<link href="https://fonts.googleapis.com/css2?family=Libre+Baskerville:ital,wght@0,400;1,400&family=Work+Sans:wght@400;500&display=swap" rel="stylesheet">
<style>
  :root {
    --navy: #2b3f99;
    --royal: #3850a8;
    --royal-deep: #23348a;
    --orange: #f08a1d;
    --sky: #3aa0d8;
    --mist: #e6f2f9;
    --white: #ffffff;
    --stage: #1c1c1f;
  }
  * { box-sizing: border-box; margin: 0; padding: 0; }
  html, body { width: 1200px; height: 963px; overflow: hidden; }
  body {
    background: var(--stage);
    font-family: "Work Sans", Arial, sans-serif;
    display: flex; align-items: center; justify-content: center; gap: 40px;
  }
  .card {
    position: relative; width: 540px; height: 310px;
    border-radius: 18px; overflow: hidden;
  }
  .card-front { background: var(--white); }
  .card-back {
    background: radial-gradient(circle at 50% 40%, var(--royal) 0%, var(--royal-deep) 100%);
    display: flex; flex-direction: column; align-items: center; justify-content: center;
  }
  .brand { display: flex; align-items: center; gap: 10px; }
  .brand-mark { width: 14px; height: 14px; background: var(--orange); flex: none; }
  .brand-name {
    font-family: "Libre Baskerville", Georgia, serif;
    font-size: 24px; letter-spacing: 1px; color: var(--navy); white-space: nowrap;
  }
  .tagline {
    font-family: "Libre Baskerville", Georgia, serif; font-style: italic;
    font-size: 12px; color: var(--orange); margin-top: 6px; white-space: nowrap;
  }
  .front-brand { position: absolute; left: 30px; top: 30px; }
  .front-brand .tagline { margin-left: 24px; }
  .divider {
    position: absolute; left: 30px; right: 30px; top: 110px;
    height: 1px; background: var(--navy);
  }
  .tree-decoration {
    position: absolute; left: 250px; top: 60px; width: 240px; height: 230px;
    border-radius: 50% 50% 40% 40%;
    background: radial-gradient(ellipse at center, var(--mist) 0%, rgba(230,242,249,0) 70%);
  }
  .contact {
    position: absolute; left: 30px; top: 124px;
    list-style: none; font-size: 11.5px; line-height: 18px; color: var(--navy);
  }
  .contact li { display: flex; align-items: center; gap: 8px; white-space: nowrap; }
  .contact .icon { width: 10px; height: 10px; flex: none; }
  .contact .spacer { width: 10px; flex: none; }
  .person { position: absolute; right: 34px; top: 150px; text-align: right; }
  .person-name {
    font-family: "Libre Baskerville", Georgia, serif;
    font-size: 19px; letter-spacing: 1px; color: var(--navy); white-space: nowrap;
  }
  .person-role { font-size: 12px; color: var(--orange); margin-top: 4px; }
  .wave { position: absolute; left: 0; bottom: 0; width: 540px; height: 90px; }
  .back-brand .brand-name { color: var(--white); font-size: 30px; }
  .back-brand .brand-mark { width: 16px; height: 16px; }
  .card-back .tagline { font-size: 14px; margin-top: 10px; }
  .website { margin-top: 34px; font-size: 12px; letter-spacing: 1.5px; color: var(--white); }
</style>
</head>
<body>
  <section class="card card-front">
    <div class="tree-decoration" role="img" aria-label="faint background decoration"></div>
    <div class="front-brand">
      <div class="brand"><span class="brand-mark"></span><span class="brand-name">BRIGHTWELL HARBOR</span></div>
      <p class="tagline">Steady steps, Open doors</p>
    </div>
    <div class="divider"></div>
    <ul class="contact">
      <li><span class="spacer"></span>480 Harbor View Rd.</li>
      <li><span class="spacer"></span>Bayside, FL 33000</li>
      <li>
        <svg class="icon" viewBox="0 0 10 10"><path d="M2 1 L4 1 L4.6 3 L3.5 4 Q4.5 6 6 6.5 L7 5.4 L9 6 L9 8 Q5 9 1 4 Z" fill="var(--orange)"/></svg>
        555-210-4836
      </li>
      <li>
        <svg class="icon" viewBox="0 0 10 10"><rect x="0.5" y="2" width="9" height="6" fill="none" stroke="var(--orange)"/><path d="M0.5 2 L5 5.5 L9.5 2" fill="none" stroke="var(--orange)"/></svg>
        hello@brightwellharbor.com
      </li>
      <li>
        <svg class="icon" viewBox="0 0 10 10"><circle cx="5" cy="5" r="4.3" fill="none" stroke="var(--orange)"/><path d="M0.7 5 H9.3 M5 0.7 Q2.5 5 5 9.3 M5 0.7 Q7.5 5 5 9.3" fill="none" stroke="var(--orange)" stroke-width="0.8"/></svg>
        www.brightwellharbor.com
      </li>
    </ul>
    <div class="person">
      <p class="person-name">DANIEL CARVER</p>
      <p class="person-role">Founder</p>
    </div>
    <svg class="wave" viewBox="0 0 540 90" preserveAspectRatio="none">
      <path d="M0 10 Q220 20 410 90 L0 90 Z" fill="var(--orange)"/>
      <path d="M0 20 Q220 30 385 90 L0 90 Z" fill="var(--navy)"/>
    </svg>
  </section>

  <section class="card card-back">
    <div class="back-brand">
      <div class="brand"><span class="brand-mark"></span><span class="brand-name">BRIGHTWELL HARBOR</span></div>
    </div>
    <p class="tagline">Steady steps, Open doors</p>
    <p class="website">www.yourwebsite.com</p>
  </section>
</body>
</html>
```